VORTALIX.CH UI Contest - design ONE App Store screenshots for a health + fitness app

Vortalix.ch is a tech incubator on a beach in Thailand and we're looking for a superstar UX/UI designer - the winner of this contest will be invited to work with us remotely and will be considered for the full incubator program!
For this contest, you will need to design ONE highly representative screenshot of an Android app. We will take all the submitted screenshots and will then A/B test them in Google Play on a selection of audiences (US M+F 14-45) - the screenshots that have the best conversion rate wins! We then would expect the winner of the content to design the final 2 screenshots for us as part of the contest.
I'm attaching an explanation of how the app works and design considerations in a ppt. The basic idea is that we have developed a mobile app that allows you to accurately track your cardio respiratory health + fitness level, stress levels and cognitive levels from your phone; without any other devices - only using your phone camera. It allows us to see what effect the things that you do in your daily life have on your fitness, cardio, stress and cognitive levels. For example for fitness, we can detect that your fitness level has improved after even 2-3 sessions of walking; while it would take you months to see the results on your body in the gym. We can detect your stress levels increasing before you are starting to get sick and notice it yourself.
We have tested the software in a marathon style event, where we test a group's levels of fitness, stress and cognitive levels then give them recommendations and test them again after a month - whoever improved the most; gets a prize.
Right now, the software acts as a basic tracker, but we are hoping to add recommendations too and that's what will inform the final design. So you set your goals, track your levels for a few days and then we provide recommendations to you, based on other folks successful experiences and on your personal level.
We are very open minded so feel free to experiment – the ideas that we have presented in the doc are not exhaustive so if you have an idea for a better screenshot/app layout/UX/UI or even an entire new concept! – email us and we can tell you if it works with our technology.
Feel free to check out pq7rm.com for an idea of a previous sports oriented app prototype that we made before.
Good luck!
Target Market(s)
Male and Female, US + EU, 14-45 age
We are looking to target people who are suffering from stress, low energy, low fitness. People who are unhappy with the way they look and feel!
Industry/Entity Type
Health And Wellness
Colors
Designer to choose colors to be used in the design.
Requirements
Must have
- Screenshots that depict the phone at least and will work well in attracting target users to download the app - they should be easy to see on a phone screen and should be colourful and appealing - check the ppt.
Nice to have
- For multiple screenshots it would be nice to have a person in the shot to make it more relatable.
Should not have
- No super sexualised images.

```html
<!DOCTYPE html>
<html lang="en">
<head>
<meta charset="utf-8">
<title>Vortalix.ch – Heart Rate screen</title>
<link href="https://fonts.googleapis.com/css2?family=Nunito+Sans:wght@400;600;700;800&display=swap" rel="stylesheet">
<style>
  :root {
    --page-bg: #e7e3dc;
    --teal: #4cf0c4;
    --teal-light: #5ef5e0;
    --teal-deep: #40e8b8;
    --screen-bg: #f3f3f3;
    --card-bg: #ffffff;
    --mint-band: #e2f5ee;
    --text-dark: #555a5c;
    --text-mid: #6b6f71;
    --text-faint: #a9b3b0;
    --track-grey: #d6d6d6;
    --white: #ffffff;
  }
  * { margin: 0; padding: 0; box-sizing: border-box; }
  html, body {
    width: 1200px; height: 963px; overflow: hidden;
    background: var(--page-bg);
    font-family: "Nunito Sans", sans-serif;
  }
  .canvas { position: relative; width: 1200px; height: 963px; }

  .app-screen {
    position: absolute; left: 352px; top: 31px;
    width: 425px; height: 771px;
    transform: scale(1.1673); transform-origin: 0 0;
    background: var(--screen-bg);
    border-radius: 28px; overflow: hidden;
    box-shadow: 0 18px 40px rgba(60, 50, 70, 0.25);
  }
  .abs { position: absolute; }

  .app-header {
    position: absolute; left: 0; top: 0; width: 425px; height: 92px;
    background: linear-gradient(100deg, var(--teal-deep) 0%, var(--teal) 45%, var(--teal-light) 100%);
    color: var(--white);
  }
  .status-bar { font-size: 11px; font-weight: 600; top: 5px; }
  .status-carrier { left: 8px; display: flex; align-items: center; gap: 3px; }
  .status-time { left: 0; width: 425px; text-align: center; }
  .status-battery { right: 8px; display: flex; align-items: center; gap: 4px; }
  .battery { width: 20px; height: 9px; background: var(--white); border-radius: 2px; }

  .brand-name {
    left: 0; top: 44px; width: 425px; text-align: center;
    font-size: 16px; font-weight: 600; color: var(--white);
  }

  .avatar {
    left: 357px; top: 39px; width: 40px; height: 40px; border-radius: 50%;
    background: radial-gradient(circle at 45% 40%, #8a7a70 0%, #4a4d55 55%, #2c3038 100%);
  }
  .menu-dots { left: 410px; top: 49px; display: flex; flex-direction: column; gap: 4px; }
  .menu-dots span { width: 4px; height: 4px; background: var(--white); border-radius: 50%; display: block; }

  .tab { top: 114px; font-size: 13px; color: var(--text-mid); }
  .tab-active { left: 25px; font-weight: 700; color: var(--text-dark); }
  .tab-stress { left: 0; width: 425px; text-align: center; }
  .tab-cognitive { right: 28px; }
  .tab-track { left: 0; top: 142px; width: 425px; height: 3px; background: var(--track-grey); }
  .tab-indicator { left: 0; top: 142px; width: 133px; height: 3px; background: var(--teal); }

  .section-title { left: 25px; font-size: 19px; font-weight: 700; color: var(--text-dark); }
  .title-heart { top: 158px; }
  .title-stats { top: 398px; }

  .chart-card {
    left: 6px; top: 192px; width: 413px; height: 153px;
    background: var(--card-bg);
    box-shadow: 0 3px 10px rgba(0,0,0,0.08);
  }
  .chart-date { left: 19px; top: 21px; font-size: 10px; color: var(--text-dark); font-weight: 600; }
  .chart-bpm { left: 92px; top: 17px; font-size: 13px; font-weight: 800; color: var(--text-dark); }
  .chart-line { left: 0; top: 0; }

  .calendar-button {
    left: 310px; top: 393px; width: 108px; height: 32px;
    background: var(--card-bg); border-radius: 3px;
    box-shadow: 0 2px 8px rgba(0,0,0,0.1);
    display: flex; align-items: center; justify-content: center; gap: 14px;
    font-size: 10px; color: var(--text-dark);
  }

  .stats-list { left: 0; top: 465px; width: 425px; height: 186px; background: var(--mint-band); }
  .stat-row { left: 25px; width: 376px; height: 40px; }
  .stat-date { font-size: 13px; color: var(--text-dark); }
  .stat-time { font-size: 9px; color: var(--text-faint); margin-top: 2px; }
  .stat-bpm { position: absolute; right: 0; top: 0; font-size: 13px; font-weight: 800; color: var(--text-dark); }

  .test-button {
    left: 122px; top: 683px; width: 181px; height: 45px;
    background: var(--teal); border-radius: 2px;
    box-shadow: 0 4px 10px rgba(76, 240, 196, 0.35);
    display: flex; align-items: center; justify-content: center; gap: 22px;
    color: var(--white); font-size: 14px; font-weight: 600;
  }
</style>
</head>
<body>
<div class="canvas">
  <div class="app-screen">
    <header class="app-header">
      <div class="abs status-bar status-carrier">●●●○○ NETLY
        <svg width="12" height="9" viewBox="0 0 12 9"><path d="M1 3.5a7 7 0 0 1 10 0M3 5.5a4 4 0 0 1 6 0" fill="none" stroke="#fff" stroke-width="1.4"/><circle cx="6" cy="7.5" r="1.2" fill="#fff"/></svg>
      </div>
      <div class="abs status-bar status-time">4:21 PM</div>
      <div class="abs status-bar status-battery">
        <svg width="7" height="10" viewBox="0 0 7 10"><path d="M1 2.5l5 5-2.5 2V0.5L6 2.5l-5 5" fill="none" stroke="#fff" stroke-width="1"/></svg>
        100% <span class="battery"></span>
      </div>
      <div class="abs brand-name">Vortalix.ch</div>
      <div class="abs avatar" role="img" aria-label="User profile photo"></div>
      <div class="abs menu-dots"><span></span><span></span><span></span></div>
    </header>

    <nav>
      <div class="abs tab tab-active">Fitness</div>
      <div class="abs tab tab-stress">Stress</div>
      <div class="abs tab tab-cognitive">Cognitive</div>
      <div class="abs tab-track"></div>
      <div class="abs tab-indicator"></div>
    </nav>

    <h2 class="abs section-title title-heart">Heart Rate</h2>
    <section class="abs chart-card">
      <div class="abs chart-date">Feb 18, 2018</div>
      <div class="abs chart-bpm">75 Bpm</div>
      <svg class="abs chart-line" width="413" height="153" viewBox="0 0 413 153">
        <polyline fill="none" stroke="#4cf0c4" stroke-width="1.6" stroke-linejoin="round"
          points="0,94 8,94 12,100 18,64 24,112 28,92 34,88 38,100 44,58 50,118 55,94 62,96 66,74 72,116 76,94 82,92 86,100 92,60 98,122 102,94 110,90 114,100 120,66 126,114 130,94 136,88 140,98 146,54 152,124 156,94 164,96 168,72 174,118 178,94 184,90 188,100 194,62 200,114 204,94 212,92 216,98 222,70 228,120 232,94 240,88 244,100 250,60 256,118 260,94 264,80 268,106 272,50 278,126 282,94 288,92 292,100 298,54 304,120 308,94 314,86 318,98 324,58 330,116 334,94 340,90 344,100 350,62 356,120 360,94 366,92 370,98 376,66 382,114 386,94 392,96 396,76 402,112 406,94 413,94"/>
      </svg>
    </section>

    <h2 class="abs section-title title-stats">Statistics</h2>
    <div class="abs calendar-button">Calendar
      <svg width="20" height="19" viewBox="0 0 20 19"><rect x="1" y="3" width="18" height="15" fill="none" stroke="#4cf0c4" stroke-width="1.8"/><path d="M6 0v5M14 0v5" stroke="#4cf0c4" stroke-width="1.8"/><g fill="#4cf0c4"><rect x="5" y="8" width="2" height="2"/><rect x="9" y="8" width="2" height="2"/><rect x="13" y="8" width="2" height="2"/><rect x="5" y="12" width="2" height="2"/><rect x="9" y="12" width="2" height="2"/><rect x="13" y="12" width="2" height="2"/></g></svg>
    </div>

    <section class="abs stats-list">
      <div class="abs stat-row" style="top:14px"><div class="stat-date">Feb 17, 2018</div><div class="stat-time">12:35am</div><div class="stat-bpm">73 Bpm</div></div>
      <div class="abs stat-row" style="top:56px"><div class="stat-date">Feb 16, 2018</div><div class="stat-time">11:25am</div><div class="stat-bpm">68 Bpm</div></div>
      <div class="abs stat-row" style="top:97px"><div class="stat-date">Feb 15, 2018</div><div class="stat-time">15:32pm</div><div class="stat-bpm">75 Bpm</div></div>
      <div class="abs stat-row" style="top:139px"><div class="stat-date">Feb 15, 2018</div><div class="stat-time">13:17am</div><div class="stat-bpm">76 Bpm</div></div>
    </section>

    <div class="abs test-button">Test Heart Rate
      <svg width="22" height="20" viewBox="0 0 22 20"><path d="M11 18.5S1.5 12.5 1.5 6.5A4.8 4.8 0 0 1 11 4.5a4.8 4.8 0 0 1 9.5 2c0 6-9.5 12-9.5 12z" fill="none" stroke="#fff" stroke-width="2" stroke-linejoin="round"/></svg>
    </div>
  </div>
</div>
</body>
</html>
```